E-Book-Design für Ejakulationstraining
Zielgruppe
Für ein E-Book im Bereich Ejakulationstraining benötigen wir ein Cover.
Aufgabenstellung
Titel: Handbuch
10 Tipps zum länger durchhalten
Es sollte in diese Richtung gehen: https://www.buchwarenlager.de/STAHL-TEMPO-Performance-Liebeskraft-Liebesleben/dp/K42X19QMTZ/ref=sr_1_1?__mk_de_DE=%C3%85M%C3%85%C5%BD%C3%95%C3%91&keywords=Stahl+Duo&qid=1566887931&s=gateway&sr=8-1

```html
<!DOCTYPE html>
<html lang="de">
<head>
<meta charset="utf-8">
<title>Handbuch – 10 Tipps zum länger durchhalten</title>
<link rel="stylesheet" href="https://fonts.googleapis.com/css2?family=Arimo:wght@400;700&display=swap">
<style>
  :root {
    --page-bg: #ffffff;
    --photo-light: #dcb9a3;
    --photo-mid: #a07868;
    --photo-dark: #3b2b26;
    --base-dark: #1d1d20;
    --brand-blue: #0b8fd3;
    --spine-blue: #1a93d6;
    --title-white: #ffffff;
  }
  * { margin: 0; padding: 0; box-sizing: border-box; }
  html, body {
    width: 940px;
    height: 1200px;
    overflow: hidden;
    background: var(--page-bg);
    font-family: "Arimo", Arial, sans-serif;
  }
  .canvas {
    position: relative;
    width: 940px;
    height: 1200px;
  }

  /* Spine */
  .spine {
    position: absolute;
    left: 172px;
    top: 50px;
    width: 42px;
    height: 1065px;
    background: linear-gradient(to bottom, var(--spine-blue) 0 740px, var(--base-dark) 740px 100%);
    overflow: hidden;
  }
  .spine-title {
    position: absolute;
    left: 4px;
    top: 30px;
    writing-mode: vertical-rl;
    font-size: 29px;
    line-height: 34px;
    letter-spacing: 3px;
    color: var(--title-white);
    white-space: nowrap;
  }
  .spine-title strong { font-weight: 700; margin-bottom: 14px; display: inline-block; }
  .spine-title span { letter-spacing: 4.4px; }

  /* Front cover */
  .cover {
    position: absolute;
    left: 214px;
    top: 50px;
    width: 636px;
    height: 1065px;
    background: var(--base-dark);
    overflow: hidden;
  }
  .cover-photo {
    position: absolute;
    left: 0;
    top: 0;
    width: 636px;
    height: 740px;
    background:
      radial-gradient(ellipse 40% 45% at 48% 35%, var(--photo-light) 0%, transparent 75%),
      radial-gradient(ellipse 35% 55% at 88% 35%, var(--photo-light) 0%, transparent 75%),
      radial-gradient(ellipse 35% 60% at 10% 70%, var(--photo-dark) 0%, transparent 80%),
      linear-gradient(170deg, var(--photo-mid) 0%, var(--photo-dark) 100%);
  }
  .title-panel {
    position: absolute;
    left: 44px;
    top: 690px;
    width: 592px;
    height: 320px;
    background: var(--brand-blue);
    color: var(--title-white);
  }
  .title-main {
    position: absolute;
    left: 30px;
    top: 24px;
    font-weight: 700;
    font-size: 85px;
    letter-spacing: 1px;
    line-height: 1;
  }
  .title-sub {
    position: absolute;
    left: 0;
    top: 126px;
    width: 564px;
    text-align: center;
    font-weight: 400;
    font-size: 62px;
    line-height: 68px;
  }
</style>
</head>
<body>
  <main class="canvas">
    <aside class="spine">
      <p class="spine-title"><strong>HANDBUCH</strong> <span>10 Tipps zum länger durchhalten</span></p>
    </aside>
    <section class="cover">
      <div class="cover-photo" role="img" aria-label="Foto: eng umschlungenes Paar, Nahaufnahme mit nassem Haar"></div>
      <div class="title-panel">
        <h1 class="title-main">HANDBUCH</h1>
        <p class="title-sub">10 Tipps zum<br>länger durchhalten</p>
      </div>
    </section>
  </main>
</body>
</html>
```